Australian Recruitment Agency Flyer

We are looking for a 1 page flyer to promote our recruitment company. We would like this to have a corporate look.

Attached is a word document with the content we would like included in the flyer.

I have also attached some of our clients logos to be included in the flyer

Target Market(s)

Professional organisations looking to hire new staff

Industry/Entity Type

It Company

Colors
85abd2
3176b5
31b7a3
d2a4cc
e667a6
b768aa
876aae
3276b5
f04a50

Requirements
Must have
• Must have the content that we have include on a word document in the design brief.

```html
<!DOCTYPE html>
<html lang="en">
<head>
<meta charset="utf-8">
<title>TalentHarbour – Recruitment Flyer</title>
<link href="https://fonts.googleapis.com/css2?family=Arimo:ital,wght@0,400;0,700;1,400;1,700&family=Raleway:wght@300&display=swap" rel="stylesheet">
<style>
  :root{
    --sky:#1aa9e0;
    --orange:#f7941d;
    --orange-dark:#e06a22;
    --navy:#262a5c;
    --blue:#27479c;
    --red:#e0234a;
    --ink:#222222;
    --heading:#2d3340;
    --grey:#3a3a3a;
    --rule:#2d3340;
  }
  *{margin:0;padding:0;box-sizing:border-box}
  html,body{width:960px;height:1200px;overflow:hidden;background:#fff}
  body{font-family:"Arimo",Arial,sans-serif;color:var(--ink)}
  .flyer{position:relative;width:960px;height:1200px;background:#fff}
  .top-bar{position:absolute;left:0;top:0;width:960px;height:24px;background:var(--sky)}

  .brand{position:absolute;left:56px;top:96px;display:flex;align-items:center;gap:18px}
  .brand-mark{width:64px;height:64px;background:var(--blue)}
  .brand-name{font-size:42px;font-weight:700;color:var(--heading);letter-spacing:-1px;line-height:1}
  .brand-sub{position:absolute;left:160px;top:176px;font-size:12.5px;color:var(--heading)}

  .headline{position:absolute;left:55px;top:250px;font-family:"Raleway",Arial,sans-serif;font-weight:300;font-size:33px;line-height:39.5px;color:var(--grey);text-transform:uppercase;letter-spacing:-1px}

  .section{position:absolute;left:547px;width:360px}
  .section h2{font-size:20px;font-weight:700;color:var(--heading);display:inline-block;width:288px;border-bottom:1.5px solid var(--rule);line-height:22px}
  .section h2 span{color:var(--sky)}
  .what{top:50px}
  .what p{margin-top:7px;font-size:16.5px;line-height:22px;color:var(--ink)}
  .industries{top:213px}
  .industries ul{list-style:none;margin-top:12px}
  .industries li{font-size:17px;line-height:31px;display:flex;align-items:center;gap:9px}
  .industries li svg{width:11px;height:15px;flex:none}

  .testimonial{position:absolute;left:0;top:443px;width:547px;height:367px;background:var(--orange)}
  .quote-mark{position:absolute;font-family:"Arimo",Arial,sans-serif;font-weight:700;font-size:190px;line-height:1;color:var(--orange-dark)}
  .quote-open{left:52px;top:-8px}
  .quote-close{left:320px;top:137px}
  .quote-text{position:absolute;right:114px;top:98px;text-align:right;font-size:17px;line-height:22px;color:var(--ink)}
  .quote-by{position:absolute;right:114px;top:262px;text-align:right;font-style:italic;font-size:17px;line-height:22px}
  .quote-by b{font-weight:700}

  .photo{position:absolute;left:547px;top:443px;width:413px;height:367px;background:linear-gradient(120deg,#1c2330 0%,#4a5466 45%,#8a8f9a 70%,#3a3f4c 100%)}

  .stripes{position:absolute;left:0;top:820px;width:960px;height:11px;display:flex}
  .stripes i{display:block;height:100%}

  .contact-band{position:absolute;left:0;top:845px;width:960px;height:93px;background:var(--sky);color:#fff;font-size:22px}
  .contact{position:absolute;top:37px;display:flex;align-items:center;gap:7px;line-height:22px}
  .contact svg{width:20px;height:20px}

  .cta{position:absolute;left:56px;top:970px;width:847px;text-align:center;font-size:30px;line-height:38.5px;color:var(--ink)}
  .cta-line{position:absolute;top:1037px;height:1.5px;background:var(--ink)}

  .client{position:absolute;top:1069px;height:63px;border:1px solid #555;display:flex;align-items:center;justify-content:center;gap:6px;font-size:15px;font-weight:700;color:var(--heading);white-space:nowrap}
  .client .dot{width:10px;height:10px;background:var(--sky)}
</style>
</head>
<body>
<div class="flyer">
  <div class="top-bar"></div>

  <div class="brand">
    <div class="brand-mark"></div>
    <div class="brand-name">TalentHarbour</div>
  </div>
  <div class="brand-sub">Human Resources &amp; Recruitment</div>

  <h1 class="headline">We have over<br>20 years of experience<br>helping companies hire<br>amazing talent</h1>

  <section class="section what">
    <h2>WHAT <span>WE DO</span></h2>
    <p>We aren’t a recruitment agency, we are an extension of your team. We become your very own HR &amp; Recruitment department to be called upon as and when needed.</p>
  </section>

  <section class="section industries">
    <h2>INDUSTRIES <span>WE SERVE</span></h2>
    <ul>
      <li><svg viewBox="0 0 11 15"><circle cx="5.5" cy="3" r="2.6" fill="#2d3340"/><rect x="4" y="6" width="3" height="9" fill="#2d3340"/></svg>Mining and Oil &amp; Gas</li>
      <li><svg viewBox="0 0 11 15"><circle cx="5.5" cy="3" r="2.6" fill="#2d3340"/><rect x="4" y="6" width="3" height="9" fill="#2d3340"/></svg>Accounting &amp; Finance</li>
      <li><svg viewBox="0 0 11 15"><circle cx="5.5" cy="3" r="2.6" fill="#2d3340"/><rect x="4" y="6" width="3" height="9" fill="#2d3340"/></svg>Sales &amp; Marketing</li>
      <li><svg viewBox="0 0 11 15"><circle cx="5.5" cy="3" r="2.6" fill="#2d3340"/><rect x="4" y="6" width="3" height="9" fill="#2d3340"/></svg>IT &amp; Communications</li>
      <li><svg viewBox="0 0 11 15"><circle cx="5.5" cy="3" r="2.6" fill="#2d3340"/><rect x="4" y="6" width="3" height="9" fill="#2d3340"/></svg>Government &amp; Not for Profit</li>
    </ul>
  </section>

  <section class="testimonial">
    <div class="quote-mark quote-open">“</div>
    <p class="quote-text">TalentHarbour really delivered on their promise<br>and far exceeded our expectations.<br>Their fixed fee model saved us thousands</p>
    <div class="quote-mark quote-close">”</div>
    <p class="quote-by"><b>Mark Ellison,</b> General Manager<br>Kestrel Financial Services</p>
  </section>

  <div class="photo" role="img" aria-label="Photo of two businesspeople in suits shaking hands"></div>

  <div class="stripes">
    <i style="width:141px;background:var(--navy)"></i>
    <i style="width:214px;background:var(--blue)"></i>
    <i style="width:192px;background:var(--sky)"></i>
    <i style="width:231px;background:var(--orange)"></i>
    <i style="width:182px;background:var(--red)"></i>
  </div>

  <div class="contact-band">
    <div class="contact" style="left:56px">
      <svg viewBox="0 0 20 20"><circle cx="10" cy="10" r="9" fill="none" stroke="#fff" stroke-width="1.6"/><path d="M7 5.5l2 2-1 1.3c.6 1.3 1.6 2.3 2.9 2.9l1.3-1 2 2-1.4 1.6C9.8 14 6.1 10.2 5.5 7z" fill="#fff"/></svg>
      000 123 4567
    </div>
    <div class="contact" style="left:257px">
      <svg viewBox="0 0 20 20"><circle cx="10" cy="10" r="9" fill="none" stroke="#fff" stroke-width="1.6"/><rect x="5" y="6.5" width="10" height="7" fill="#fff"/><path d="M5 6.5l5 4 5-4" fill="none" stroke="#1aa9e0" stroke-width="1.2"/></svg>
      your email address.com.au
    </div>
    <div class="contact" style="left:600px">
      <svg viewBox="0 0 20 20"><circle cx="10" cy="10" r="9" fill="none" stroke="#fff" stroke-width="1.6"/><circle cx="10" cy="10" r="5.5" fill="none" stroke="#fff" stroke-width="1.2"/><path d="M4.5 10h11M10 4.5c-2.5 3-2.5 8 0 11M10 4.5c2.5 3 2.5 8 0 11" fill="none" stroke="#fff" stroke-width="1"/></svg>
      www.yourwebsite.com.au
    </div>
  </div>

  <p class="cta">Start a conversation today and see why these&nbsp; companies<br>turn to us time and time again</p>
  <div class="cta-line" style="left:56px;width:200px"></div>
  <div class="cta-line" style="left:703px;width:200px"></div>

  <div class="client" style="left:56px;width:142px">Fleetwise</div>
  <div class="client" style="left:205px;width:99px">KFS</div>
  <div class="client" style="left:311px;width:84px">QTX</div>
  <div class="client" style="left:401px;width:117px">Spodumen Co</div>
  <div class="client" style="left:525px;width:173px"><span class="dot"></span>Halden Process</div>
  <div class="client" style="left:705px;width:82px;font-size:10px">SOUTHRIDGE</div>
  <div class="client" style="left:794px;width:109px">ORBIT</div>
</div>
</body>
</html>
```